TIME BAR Design Project

DESIGN: TIME LAPSE BAR

We are looking for a fresh design for a time lapse bar which would appear on screen during an exercise video.

Please see a quick example attached. We would like it to be created in Photoshop or Illustrator, in layers. ( no after effects please).

We need a layer that would move to indicate the time passing.

We would like to manipulate the time as needed for various pieces.
Updates

Quick update:
please note the current bar in the sample picts was done in-house and is only intended to be a guide.  The bar does not have to resemble the sample. Thanks.

Target Market(s)

male /female 25-65 60% women.

Requirements
Must have
• Created in Photoshop or Illustrator.

Minimum 300DPI.

Please see that there is needs to be a place for the name of each exercise - this can appear and then fade out.
Nice to have
• -bar should match the mood of the set and colors.( see picts).

-bar CAN BE see-through so that the body's are seen behind it.
Should not have
• too high tech or masculine

too feminine

```html
<!DOCTYPE html>
<html lang="en">
<head>
<meta charset="utf-8">
<title>Time Lapse Bar</title>
<link rel="stylesheet" href="https://fonts.googleapis.com/css2?family=Arimo:wght@700&display=swap">
<style>
  :root {
    --page: #ffffff;
    --letterbox: #000000;
    --frame-grey: #8c8c8c;
    --frame-edge: #6e6e6e;
    --track: #ffffff;
    --track-clear: rgba(255, 255, 255, 0.35);
    --silver-light: #f4f4f4;
    --silver-mid: #d6d6d6;
    --silver-dark: #9a9a9a;
    --label: #ffffff;
    --studio-wall: #e9e1d3;
    --studio-trim: #d98b3a;
    --studio-floor: #d7a05e;
  }
  * { box-sizing: border-box; margin: 0; padding: 0; }
  html, body { width: 1200px; height: 900px; overflow: hidden; background: var(--page); }
  body { position: relative; font-family: "Arimo", Arial, sans-serif; }

  .video-still {
    position: absolute; left: 0; top: 0; width: 1200px; height: 680px;
    background: linear-gradient(180deg, var(--studio-wall) 0%, #e4d6c0 42%, var(--studio-trim) 55%, var(--studio-floor) 62%, #e0b27a 100%);
  }
  .letterbox {
    position: absolute; left: 0; top: 678px; width: 1200px; height: 37px;
    background: var(--letterbox);
  }

  .time-bar {
    position: absolute; display: flex; align-items: center;
    background: var(--frame-grey);
    border: 2px solid var(--frame-edge);
  }
  .time-bar__track { position: relative; height: 100%; }
  .time-bar__progress {
    position: absolute; left: 0; top: 0; bottom: 0;
    background: linear-gradient(180deg, var(--silver-dark) 0%, var(--silver-light) 22%, var(--silver-mid) 55%, var(--silver-light) 78%, var(--silver-dark) 100%);
    border-radius: 3px;
  }
  .time-bar__label {
    flex: 1; text-align: center; color: var(--label);
    font-weight: 700; letter-spacing: 0.3px;
  }

  .time-bar--overlay {
    left: 293px; top: 570px; width: 636px; height: 43px;
    border-radius: 5px; padding: 4px 0 4px 5px;
  }
  .time-bar--overlay .time-bar__track { width: 477px; background: var(--track-clear); }
  .time-bar--overlay .time-bar__progress { width: 411px; }
  .time-bar--overlay .time-bar__label { font-size: 17px; }

  .time-bar--full {
    left: 22px; top: 774px; width: 1156px; height: 78px;
    border-radius: 9px; padding: 8px 0 8px 12px;
  }
  .time-bar--full .time-bar__track { width: 865px; background: var(--track); }
  .time-bar--full .time-bar__progress { width: 744px; box-shadow: 4px 0 6px rgba(0,0,0,0.25); }
  .time-bar--full .time-bar__label { font-size: 33px; }
</style>
</head>
<body>
  <div class="video-still" role="img" aria-label="Exercise video still: two instructors in a bright studio with a wooden floor, shaking flexible training blades"></div>
  <div class="letterbox"></div>

  <div class="time-bar time-bar--overlay">
    <div class="time-bar__track"><div class="time-bar__progress"></div></div>
    <div class="time-bar__label">FLEXWAND</div>
  </div>

  <div class="time-bar time-bar--full">
    <div class="time-bar__track"><div class="time-bar__progress"></div></div>
    <div class="time-bar__label">FLEXWAND</div>
  </div>
</body>
</html>
```